new dating app design - young, fresh, clean

Project Brief

Vimzy is the world's first dating app that actually arranges dates. The process consists of 3 easy steps:

1. use our calendar to tell us when you'd like a date
2. browse singles nearby and select who you'd like to meet
3. when your date is 1 hour away, the app will find you a nice venue in the neighborhood and send one of your matches there to meet you. All you need to do is show up and have a good time.

This design assignment consists of creating a fun, fresh & user-friendly design for the wireframes created by our UX designer. Included are 2 screens:

1. the 'calendar' screen

2. the 'matches' screen

Also included is our style guide for your reference. Feel free to use as much or as little from this guide as you please. It would be nice if we could remain somewhat consistent with our previous design (which was purely based on this style guide) but we also want you to be creative and show off your skills so by no means should you feel obliged to conform to it.

Things to consider

1. 'calendar'

this is where you tell the app when you're free for a date. You can select as many time slots as you want. The info bars at the top and the bottom are 'sticky' (will stay in place no matter where in the screen you scroll to).

Everything about this page needs to be designed: not just in terms of spacing, font and coloring of the calendar itself but also the sticky bars at the bottom and top, and the interactions (when you select a time slot, what happens visually? How will it show that this slot was selected?).

TIP: please ignore the black vs white time slot distribution you see in the image. This was meant to signify where daytime becomes nighttime and vice versa, but we're not doing that anymore. So the only difference between blocks will be the difference between a selected and an unselected block. Make sure that difference is clearly visible in your design.

2. 'matches'

this is where you tell the app whom you'd like to meet with. You can select as many people as you want by clicking their 'heart' icon. You can scroll down to see more people and again the info bars at the top and/or bottom are sticky. The design elements for this page are:

a. the page itself (sizing, spacing of the images, etc.)
b. the interactions (how does a selected heart look, how does that compare to an unselected heart)

ICONS: feel free to come up with your own iconography (ie for the 'chat' icon in the top right, and/or the 'heart' icon signifying you want to meet this person. We really like the fact that the 'matches' and 'calendar' tabs are signified with words rather than icons, but feel free to get creative on this front as well. If you can make it prettier, we're all ears :) Whatever you do on this front, make sure all your icons and the rest of your work are/is free of copyright so we can actually use them in a commercially distributed app.

The winner of this contest may get awarded a follow-up project where they will be asked to design the entire app for us.

Reason: Thank you all for your submissions. We got some promising designs but nothing that was good enough just yet. We gave some feedback for improvement and wanted to give you guys some more time to get it right. New submissions are welcome too of course. Don't hesitate to contact us if you have any questions.

Target Market(s)

singles

Industry/Entity Type

Dating

Requirements
Must have
• fresh, clean, user-friendly design of the 2 pages provided. Your design choices should include decisions about font, sizing, colours, spacing, etc.
Nice to have
• custom icons, see project brief

```html
<!DOCTYPE html>
<html lang="en">
<head>
<meta charset="utf-8">
<title>Vimzy – Matches &amp; Schedule</title>
<link href="https://fonts.googleapis.com/css2?family=Roboto+Condensed:wght@300;400&family=Roboto:wght@300;400;500&display=swap" rel="stylesheet">
<style>
  :root{
    --bg:#ef4a55;
    --red:#e8194f;
    --red-soft:#f05a6a;
    --pink:#f6a3b6;
    --white:#ffffff;
    --ink:#e1262e;
    --cyan:#22b3ea;
    --slot-on:#8b8b8b;
    --grid-line:#e9e9e9;
    --photo-a:#d9d9d9;
    --photo-b:#3b3b3b;
  }
  *{box-sizing:border-box;margin:0;padding:0}
  html,body{width:1200px;height:1200px;overflow:hidden}
  body{background:var(--bg);font-family:"Roboto Condensed",sans-serif;position:relative}

  .screen{position:absolute;top:227px;width:420px;height:747px;background:var(--white);overflow:hidden;box-shadow:0 20px 50px rgba(120,0,20,.25)}
  .screen--matches{left:150px}
  .screen--schedule{left:630px}

  /* header */
  .app-header{position:relative;height:160px;background:linear-gradient(100deg,var(--red) 0%,var(--red) 45%,var(--pink) 100%);color:var(--white)}
  .status-bar{height:24px;display:flex;align-items:center;justify-content:space-between;padding:0 10px;font-family:"Roboto",sans-serif;font-size:12px;font-weight:300}
  .status-bar .carrier{letter-spacing:.5px}
  .status-bar .battery{display:flex;align-items:center;gap:4px}
  .title-row{display:flex;align-items:center;padding:14px 18px 0;gap:16px}
  .title-row .app-title{font-size:28px;font-weight:400;flex:1}
  .tabs{position:absolute;left:18px;right:18px;bottom:22px;display:flex;justify-content:space-between;align-items:center}
  .tab{height:42px;padding:0 26px;border-radius:21px;border:2px solid var(--white);font-size:20px;font-weight:300;display:flex;align-items:center;color:var(--white);letter-spacing:.5px}
  .tab--active{background:var(--white);color:var(--red-soft)}
  .tabs::before{content:"";position:absolute;left:120px;right:150px;top:50%;height:2px;background:var(--white)}

  /* matches grid */
  .match-grid{display:grid;grid-template-columns:repeat(3,1fr);padding:22px 14px 0;row-gap:18px}
  .match{display:flex;flex-direction:column;align-items:center;gap:8px}
  .avatar{position:relative;width:108px;height:108px;border-radius:50%;border:8px solid var(--red);background:radial-gradient(circle at 60% 40%,var(--photo-a),var(--photo-b) 75%)}
  .avatar--picked{border-color:var(--pink);opacity:.7}
  .heart-badge{position:absolute;left:50%;top:50%;width:26px;height:26px;margin:-4px 0 0 -13px;border-radius:50%;background:var(--white);border:2px solid var(--red);display:flex;align-items:center;justify-content:center}
  .match-name{font-size:22px;color:var(--cyan);font-weight:400}

  .sticky-footer{position:absolute;left:0;right:0;bottom:0;height:86px;background:var(--red-soft);color:var(--white);font-size:19px;font-weight:300;padding:16px 24px;line-height:1.35}
  .inline-heart{display:inline-flex;width:20px;height:20px;border-radius:50%;background:var(--white);vertical-align:-3px;align-items:center;justify-content:center}

  /* schedule */
  .notice{position:relative;margin:-4px 14px 0;height:64px;background:var(--ink);color:var(--white);border-radius:6px;font-size:16px;font-weight:300;padding:12px 40px;line-height:1.3}
  .notice .q{position:absolute;font-size:36px;font-weight:400;line-height:1}
  .notice .q--open{left:10px;top:6px}
  .notice .q--close{right:12px;bottom:-6px}
  .notice::after{content:"";position:absolute;right:16px;bottom:-12px;border-left:14px solid transparent;border-top:14px solid var(--ink)}
  .slot-grid{display:grid;grid-template-columns:repeat(3,1fr);margin-top:18px}
  .slot{height:84px;border-right:1px solid var(--grid-line);border-bottom:1px solid var(--grid-line);display:flex;flex-direction:column;align-items:center;justify-content:center;color:var(--ink);font-family:"Roboto",sans-serif}
  .slot:nth-child(3n){border-right:none}
  .slot .time{font-size:40px;font-weight:500;line-height:1}
  .slot .date{font-size:11px;font-weight:300;margin-top:4px}
  .slot--selected{background:var(--slot-on);color:var(--white);border-color:#7a7a7a}
</style>
</head>
<body>

<!-- Matches screen -->
<section class="screen screen--matches">
  <header class="app-header">
    <div class="status-bar">
      <span class="carrier">●●●○○ NOVA</span>
      <span class="clock">4:21 PM</span>
      <span class="battery">100%
        <svg width="24" height="11" viewBox="0 0 24 11"><rect x="0.5" y="0.5" width="21" height="10" rx="2" fill="none" stroke="#fff"/><rect x="2" y="2" width="18" height="7" fill="#fff"/><rect x="22" y="3.5" width="1.5" height="4" fill="#fff"/></svg>
      </span>
    </div>
    <div class="title-row">
      <svg width="30" height="26" viewBox="0 0 30 26" aria-label="Menu"><g stroke="#fff" stroke-width="3"><line x1="0" y1="3" x2="30" y2="3"/><line x1="0" y1="13" x2="22" y2="13"/><line x1="0" y1="23" x2="30" y2="23"/></g></svg>
      <span class="app-title">Vimzy home</span>
      <svg width="40" height="38" viewBox="0 0 40 38" aria-label="Chat"><g fill="none" stroke="#fff" stroke-width="2"><path d="M8 4h30v20H20l-6 6v-6H8z"/><path d="M2 10h4M2 10v20h6v6l6-6"/></g></svg>
    </div>
    <nav class="tabs">
      <span class="tab tab--active">MATCHES</span>
      <span class="tab">SCHEDULE</span>
    </nav>
  </header>

  <div class="match-grid">
    <div class="match"><div class="avatar" role="img" aria-label="Profile photo of a match"><span class="heart-badge"><svg width="14" height="13" viewBox="0 0 14 13"><path d="M7 12L1.5 6.5A3.2 3.2 0 0 1 7 2a3.2 3.2 0 0 1 5.5 4.5z" fill="#22b3ea"/></svg></span></div><span class="match-name">Maren</span></div>
    <div class="match"><div class="avatar" role="img" aria-label="Profile photo of a match"><span class="heart-badge"><svg width="14" height="13" viewBox="0 0 14 13"><path d="M7 12L1.5 6.5A3.2 3.2 0 0 1 7 2a3.2 3.2 0 0 1 5.5 4.5z" fill="#22b3ea"/></svg></span></div><span class="match-name">Maren</span></div>
    <div class="match"><div class="avatar avatar--picked" role="img" aria-label="Profile photo of a selected match"><span class="heart-badge"><svg width="14" height="13" viewBox="0 0 14 13"><path d="M7 12L1.5 6.5A3.2 3.2 0 0 1 7 2a3.2 3.2 0 0 1 5.5 4.5z" fill="#22b3ea"/></svg></span></div><span class="match-name">Maren</span></div>
    <div class="match"><div class="avatar" role="img" aria-label="Profile photo of a match"><span class="heart-badge"><svg width="14" height="13" viewBox="0 0 14 13"><path d="M7 12L1.5 6.5A3.2 3.2 0 0 1 7 2a3.2 3.2 0 0 1 5.5 4.5z" fill="#22b3ea"/></svg></span></div><span class="match-name">Maren</span></div>
    <div class="match"><div class="avatar" role="img" aria-label="Profile photo of a match"><span class="heart-badge"><svg width="14" height="13" viewBox="0 0 14 13"><path d="M7 12L1.5 6.5A3.2 3.2 0 0 1 7 2a3.2 3.2 0 0 1 5.5 4.5z" fill="#22b3ea"/></svg></span></div><span class="match-name">Maren</span></div>
    <div class="match"><div class="avatar" role="img" aria-label="Profile photo of a match"><span class="heart-badge"><svg width="14" height="13" viewBox="0 0 14 13"><path d="M7 12L1.5 6.5A3.2 3.2 0 0 1 7 2a3.2 3.2 0 0 1 5.5 4.5z" fill="#22b3ea"/></svg></span></div><span class="match-name">Maren</span></div>
    <div class="match"><div class="avatar" role="img" aria-label="Profile photo of a match"><span class="heart-badge"><svg width="14" height="13" viewBox="0 0 14 13"><path d="M7 12L1.5 6.5A3.2 3.2 0 0 1 7 2a3.2 3.2 0 0 1 5.5 4.5z" fill="#22b3ea"/></svg></span></div><span class="match-name">Maren</span></div>
    <div class="match"><div class="avatar" role="img" aria-label="Profile photo of a match"><span class="heart-badge"><svg width="14" height="13" viewBox="0 0 14 13"><path d="M7 12L1.5 6.5A3.2 3.2 0 0 1 7 2a3.2 3.2 0 0 1 5.5 4.5z" fill="#22b3ea"/></svg></span></div><span class="match-name">Maren</span></div>
    <div class="match"><div class="avatar" role="img" aria-label="Profile photo of a match"><span class="heart-badge"><svg width="14" height="13" viewBox="0 0 14 13"><path d="M7 12L1.5 6.5A3.2 3.2 0 0 1 7 2a3.2 3.2 0 0 1 5.5 4.5z" fill="#22b3ea"/></svg></span></div><span class="match-name">Maren</span></div>
  </div>

  <footer class="sticky-footer">
    Excellent! You can <span class="inline-heart"><svg width="12" height="11" viewBox="0 0 14 13"><path d="M7 12L1.5 6.5A3.2 3.2 0 0 1 7 2a3.2 3.2 0 0 1 5.5 4.5z" fill="#22b3ea"/></svg></span> more if you do like.<br>
    Next, share your schedule with us!
  </footer>
</section>

<!-- Schedule screen -->
<section class="screen screen--schedule">
  <header class="app-header">
    <div class="status-bar">
      <span class="carrier">●●●○○ NOVA</span>
      <span class="clock">4:21 PM</span>
      <span class="battery">100%
        <svg width="24" height="11" viewBox="0 0 24 11"><rect x="0.5" y="0.5" width="21" height="10" rx="2" fill="none" stroke="#fff"/><rect x="2" y="2" width="18" height="7" fill="#fff"/><rect x="22" y="3.5" width="1.5" height="4" fill="#fff"/></svg>
      </span>
    </div>
    <div class="title-row">
      <svg width="30" height="26" viewBox="0 0 30 26" aria-label="Menu"><g stroke="#fff" stroke-width="3"><line x1="0" y1="3" x2="30" y2="3"/><line x1="0" y1="13" x2="22" y2="13"/><line x1="0" y1="23" x2="30" y2="23"/></g></svg>
      <span class="app-title">Vimzy home</span>
      <svg width="40" height="38" viewBox="0 0 40 38" aria-label="Chat"><g fill="none" stroke="#fff" stroke-width="2"><path d="M8 4h30v20H20l-6 6v-6H8z"/><path d="M2 10h4M2 10v20h6v6l6-6"/></g></svg>
    </div>
    <nav class="tabs">
      <span class="tab tab--active">MATCHES</span>
      <span class="tab">SCHEDULE</span>
    </nav>
  </header>

  <div class="notice">
    <span class="q q--open">“</span>
    Choose when you are available.<br>We will schedule your dates for you!
    <span class="q q--close">”</span>
  </div>

  <div class="slot-grid">
    <div class="slot"><span class="time">13:00</span><span class="date">18 Tue 2017</span></div>
    <div class="slot"><span class="time">14:00</span><span class="date">18 Tue 2017</span></div>
    <div class="slot"><span class="time">15:00</span><span class="date">18 Tue 2017</span></div>
    <div class="slot"><span class="time">16:00</span><span class="date">18 Tue 2017</span></div>
    <div class="slot slot--selected"><span class="time">17:00</span><span class="date">18 Tue 2017</span></div>
    <div class="slot slot--selected"><span class="time">18:00</span><span class="date">18 Tue 2017</span></div>
    <div class="slot slot--selected"><span class="time">19:00</span><span class="date">18 Tue 2017</span></div>
    <div class="slot slot--selected"><span class="time">20:00</span><span class="date">18 Tue 2017</span></div>
    <div class="slot slot--selected"><span class="time">21:00</span><span class="date">18 Tue 2017</span></div>
    <div class="slot"><span class="time">21:00</span><span class="date">18 Tue 2017</span></div>
    <div class="slot"><span class="time">22:00</span><span class="date">18 Tue 2017</span></div>
    <div class="slot"><span class="time">23:00</span><span class="date">18 Tue 2017</span></div>
    <div class="slot"><span class="time">00:00</span><span class="date">19 Wed 2017</span></div>
    <div class="slot"><span class="time">01:00</span><span class="date">19 Wed 2017</span></div>
    <div class="slot"><span class="time">02:00</span><span class="date">19 Wed 2017</span></div>
    <div class="slot"><span class="time">03:00</span><span class="date">19 Wed 2017</span></div>
    <div class="slot"><span class="time">04:00</span><span class="date">19 Wed 2017</span></div>
    <div class="slot"><span class="time">05:00</span><span class="date">19 Wed 2017</span></div>
  </div>
</section>

</body>
</html>
```